Design a van wrap

We require a full van wrap design for a construction and development company. The design must present a premium, professional, and highly visible brand image suitable for a modern construction business. See attached existing wrap. Require a whole new look.
Vehicle Details
- Vehicle: Velbro electric van (T7 / similar size)
- Wrap type: Full wrap (bonnet, sides, rear)
- Use Palmet image on the rear doors
Dimension uCarrio 8 L1H1 uCarrio 8 L2H1
Overall length ~4,800 mm ~5,250 mm
Overall width (excl. mirrors) ~1,874 mm ~1,874 mm
Overall height (H1) ~1,960 mm ~1,960 mm
Wheelbase ~3,100 mm ~3,450 mm
Roof height H1 (standard) H1 (standard)
Branding
- Company Name: KORVELT
- Industry: Construction & Development
- 4 bullets on each side of van detailing scope of business
- New Builds
- Basement Works
- Piling Works
- Demolition
- Engineering
- RC Frame Works
- Loft Conversions
- Refurbishment
Brand Style: Modern, strong, premium, clean
- Colours:
- Primary: Black and Brown
- Accent: Cream (for contrast and legibility if required - see business card)
- Existing assets: Logo will be provided (vector format)
Design Style & Finish
- Contemporary and bold
- Strong contrast for roadside visibility
- Suitable for commercial vinyl printing
- Avoid over-complication or excessive textures
Deliverables
- Print-ready files
- Vector format preferred (AI / EPS / PDF)
- High-resolution mockups showing all sides of the van
- Colour codes specified (CMYK / Pantone if applicable)
Target Outcome
A van wrap that clearly communicates professionalism, scale, and trust, stands out on the road, and reinforces a premium construction brand.

```html
<!DOCTYPE html>
<html lang="en">
<head>
<meta charset="utf-8">
<title>KORVELT Van Wrap</title>
<link href="https://fonts.googleapis.com/css2?family=Montserrat:wght@700;800&display=swap" rel="stylesheet">
<style>
  :root{
    --tan:#c6b293;
    --charcoal:#2a2829;
    --black:#111111;
    --cream:#d9c7a6;
    --glass:#3a3a3c;
    --lamp:#4a1517;
    --tyre:#1b1b1b;
    --hub:#e4e4e4;
    --bg:#ffffff;
  }
  html,body{margin:0;padding:0;overflow:hidden;background:var(--bg);}
  .canvas{position:relative;width:1200px;height:1200px;overflow:hidden;background:var(--bg);font-family:"Montserrat",sans-serif;}
  .artwork{position:absolute;left:0;top:0;}
  .side-logo{position:absolute;left:182px;top:120px;width:239px;height:215px;border:6px solid var(--black);
    display:flex;flex-direction:column;align-items:center;justify-content:center;gap:22px;}
  .brand-square{width:90px;height:90px;background:var(--black);flex:none;}
  .brand-name{font-weight:800;color:var(--black);line-height:1;white-space:nowrap;}
  .side-logo .brand-name{font-size:28px;letter-spacing:6px;margin-right:-6px;}
  .scope-list{position:absolute;left:442px;top:156px;margin:0;padding:0;list-style:none;
    color:var(--cream);font-weight:700;font-size:18.5px;line-height:24px;}
  .scope-list li::before{content:"•";margin-right:8px;}
  .side-phone{position:absolute;left:450px;top:272px;font-weight:800;font-size:51px;color:var(--black);letter-spacing:-1px;white-space:nowrap;}
  .side-web{position:absolute;left:481px;top:330px;font-weight:700;font-size:30px;color:var(--black);white-space:nowrap;}
  .rear-logo{position:absolute;left:431px;top:611px;display:flex;align-items:center;gap:11px;}
  .rear-logo .brand-square{width:53px;height:53px;}
  .rear-logo .brand-name{font-size:42px;letter-spacing:8px;}
  .rear-photo{position:absolute;left:498px;top:668px;width:190px;height:172px;border:6px solid var(--black);
    background:linear-gradient(180deg,#b8cde0 0%,#d9e3ec 30%,#c9652f 55%,#b05224 85%,#9a9a96 100%);}
  .rear-phone{position:absolute;left:0;width:1200px;top:852px;text-align:center;padding-left:4px;box-sizing:border-box;
    font-weight:800;font-size:33px;color:var(--black);letter-spacing:-0.5px;}
  .rear-web{position:absolute;left:0;width:1200px;top:890px;text-align:center;padding-left:6px;box-sizing:border-box;font-weight:700;font-size:19.5px;color:var(--black);}
</style>
</head>
<body>
<main class="canvas">
  <svg class="artwork" width="1200" height="1200" viewBox="0 0 1200 1200" aria-hidden="true">
    <g class="van-side">
      <path d="M150 112 L690 105 Q760 105 800 125 L905 225 Q1040 250 1062 285 L1065 410 Q1062 425 1045 425 L145 425 Q138 420 138 400 L140 130 Q142 114 150 112 Z" fill="var(--tan)"/>
      <path d="M433 144 L670 144 L670 128 L790 128 L905 228 Q1010 240 1060 290 L870 290 L870 270 L433 270 Z" fill="var(--charcoal)"/>
      <path d="M675 132 L782 132 L860 215 L675 236 Z" fill="var(--glass)"/>
      <rect x="138" y="140" width="40" height="180" fill="var(--charcoal)"/>
      <rect x="146" y="195" width="24" height="120" rx="6" fill="var(--lamp)"/>
      <rect x="138" y="400" width="927" height="25" fill="var(--black)"/>
      <circle cx="312" cy="415" r="72" fill="var(--bg)"/>
      <circle cx="890" cy="415" r="72" fill="var(--bg)"/>
      <circle cx="312" cy="415" r="64" fill="var(--tyre)"/>
      <circle cx="890" cy="415" r="64" fill="var(--tyre)"/>
      <circle cx="312" cy="415" r="42" fill="var(--hub)"/>
      <circle cx="890" cy="415" r="42" fill="var(--hub)"/>
    </g>
    <g class="van-rear">
      <path d="M384 592 Q390 580 420 580 L790 580 Q818 580 824 592 L860 700 L863 990 L344 990 L347 700 Z" fill="var(--tan)"/>
      <rect x="385" y="680" width="435" height="172" fill="var(--charcoal)"/>
      <rect x="347" y="705" width="40" height="170" rx="10" fill="var(--lamp)"/>
      <rect x="820" y="705" width="42" height="170" rx="10" fill="var(--lamp)"/>
      <rect x="398" y="920" width="412" height="72" rx="10" fill="var(--charcoal)"/>
      <rect x="425" y="942" width="138" height="28" fill="var(--hub)"/>
      <rect x="346" y="990" width="517" height="40" rx="8" fill="var(--black)"/>
      <rect x="356" y="1030" width="62" height="42" rx="10" fill="var(--tyre)"/>
      <rect x="790" y="1030" width="62" height="42" rx="10" fill="var(--tyre)"/>
      <line x1="603" y1="585" x2="603" y2="990" stroke="var(--charcoal)" stroke-width="1.5" opacity="0.5"/>
    </g>
  </svg>

  <div class="side-logo">
    <span class="brand-square"></span>
    <span class="brand-name">KORVELT</span>
  </div>
  <ul class="scope-list">
    <li>New Builds</li>
    <li>Basement Works</li>
    <li>Piling Works</li>
    <li>Demolition</li>
  </ul>
  <div class="side-phone">0800 5520 174</div>
  <div class="side-web">www.korvelt.co.uk</div>

  <div class="rear-logo">
    <span class="brand-square"></span>
    <span class="brand-name">KORVELT</span>
  </div>
  <div class="rear-photo" role="img" aria-label="Photograph of a completed development: a modern six-storey orange brick apartment block with balconies under a pale blue sky"></div>
  <div class="rear-phone">0800 5520 174</div>
  <div class="rear-web">www.korvelt.co.uk</div>
</main>
</body>
</html>
```